Lens Deal Ranger

This website is a price comparison site specialising in Digital Photographic equipment - DSLR Cameras & Lenses etc. It is going to operate along the lines of a site called www.shuttertallyhub.example
It must look much more professional and less home made than the afforementioned site. My site will be a direct competitor to shuttertallyhub, so it must look and operate much better.
The new site is first and foremost a price information site - it is not selling anything! The message it should send to visitors is one of impartiality and unbiased information, the shops it links to are the ones who will be selling products. People who visit this site, have already decided which product they are going to buy, they are now at the stage of looking for which shop is offering the best deal based on PRICE. This is NOT a "WHAT CAMERA" site. This site is comparing DIFFERENT PRICES for the same product offered by a list of SHOPS. The site should look expensive. I have a couple of Logos which you can look at for colour ideas. I like Blue, Silver, aluminium, stainless steel, White, Grey and Black. There must be lots of product category buttons to chose from. If you can come up with anything imaginative, I will appreciate any clever ideas. Some flash technology might be nice or something visually interesting happening to catch the visitors attention. There are lots of stock photos available on the net of the kind of products we will be dealing with. In particular VORTELL and KASURO Digital SLR Cameras and Lenses. All the other brands are definately second division. There will be no telephone number on the page. My Logo will be at the top of the page. I have uploaded two logos for you to take your pick and a very nice picture of a very expensivr DSLR camera which you might want to utilize.

Target Market(s)

Buyers of DSLR Camera equipment 70% Male, Age group 35 to 70. The products being compared on this site are all high ticket items. Customers are usually quite well off.

Industry/Entity Type

Camera

Requirements
Must have
• Must be simple and easy to navigate to find the desired product very easily.
Nice to have
• Should have a space on the front page for "TODAYS PRICE DROPS"

```html
<!DOCTYPE html>
<html lang="en">
<head>
<meta charset="utf-8">
<title>Lens Deal Ranger</title>
<link rel="stylesheet" href="https://fonts.googleapis.com/css2?family=Source+Sans+3:wght@400;600&display=swap">
<style>
:root{
  --blue:#2f8fcf;
  --navy:#1d4472;
  --text:#3a3a3a;
  --muted:#9a9a9a;
  --line:#dcdcdc;
  --panel:#f1f1f1;
  --tab:#a9a9a9;
  --white:#ffffff;
}
*{margin:0;padding:0;box-sizing:border-box}
html,body{width:1200px;height:901px;overflow:hidden;background:var(--white)}
body{position:relative;font-family:"Source Sans 3",Arial,sans-serif;color:var(--text)}
.viewport{position:absolute;left:0;top:0;width:1200px;height:901px;overflow:hidden}
.page{position:absolute;left:0;top:0;width:1100px;height:826px;overflow:hidden;transform:scale(1.0909);transform-origin:0 0}
.abs{position:absolute}

/* header */
.brand{left:86px;top:30px;width:140px;text-align:center}
.brand-dot{display:block;margin:0 auto 8px;width:54px;height:54px;border-radius:50%;background:var(--blue)}
.brand-name{font-size:15px;font-weight:600;color:var(--navy);letter-spacing:.5px;text-transform:uppercase}
.compare{left:722px;top:72px;display:flex;gap:10px;align-items:flex-start}
.compare-title{font-size:14px;color:var(--blue);line-height:16px}
.compare-count{font-size:11px;color:var(--muted)}
.nav-link{top:72px;width:60px;text-align:center;font-size:12px;color:var(--blue)}
.nav-link svg{display:block;margin:0 auto 4px}

/* filter panel */
.filters{left:68px;top:129px;width:956px;height:300px;background:var(--panel);box-shadow:0 1px 3px rgba(0,0,0,.25)}
.tabs{left:0;top:0;width:58px;height:300px;background:var(--tab)}
.tab{position:absolute;left:0;width:58px;height:51px}
.tab.active{background:var(--panel)}
.tab-thumb{position:absolute;left:15px;width:28px;height:26px;border-radius:4px;background:linear-gradient(#555,#1c1c1c)}
.group{position:absolute;width:180px;height:150px;border-right:1px solid var(--line);border-bottom:1px solid var(--line);padding:17px 0 0 10px}
.group h3{font-size:14px;font-weight:400;color:var(--blue);margin-bottom:7px}
.group ul{list-style:none}
.group li{font-size:12px;line-height:18px;padding-left:18px;position:relative}
.group li::before{content:"";position:absolute;left:1px;top:6px;width:7px;height:7px;border:1px solid #c4c4c4;background:#fafafa}
.group li.on::before{background:#555;box-shadow:inset 0 0 0 1px #fff}
.group li span{color:var(--muted)}
.more{position:absolute;right:10px;top:129px;font-size:11px;color:var(--blue);display:flex;align-items:center;gap:3px}
.more i{display:inline-block;width:9px;height:9px;background:var(--blue)}
.price-input{position:absolute;top:57px;width:64px;height:23px;background:#fff;border:1px solid #ddd;font-size:12px;padding:4px 0 0 4px}
.to{position:absolute;left:84px;top:61px;font-size:12px}
.scale-label{position:absolute;top:98px;font-size:11px;color:var(--muted)}
.track{position:absolute;left:10px;top:125px;width:156px;height:5px;background:#ddd;border-radius:3px}
.track-fill{position:absolute;left:24px;width:80px;height:5px;background:var(--blue)}
.knob{position:absolute;top:-4px;width:13px;height:13px;border-radius:50%;background:#fff;border:3px solid var(--blue)}

.search{left:856px;top:430px;width:158px;height:30px;background:linear-gradient(#f4f4f4,#e2e2e2);display:flex;align-items:center;justify-content:center;gap:8px;font-size:14px;color:var(--blue)}

/* sidebar */
.sidebar{left:68px;top:471px;width:228px;height:355px;overflow:hidden;list-style:none}
.sidebar li{height:36px;line-height:36px;font-size:14px;border-bottom:1px solid #e6e6e6;padding-left:9px}
.sidebar li span{color:var(--muted)}
.sidebar .maker{background:linear-gradient(#ececec,#dadada);border-bottom:1px solid #fff}
.sidebar .current{color:var(--blue)}
.sidebar .sub{padding-left:27px}
.sidebar .leaf{padding-left:45px}

/* products */
.section-icon{left:326px;top:472px}
.section-title{left:374px;top:481px;font-size:22px;color:var(--blue);font-weight:400}
.card{top:545px;width:218px;height:281px;overflow:hidden;border:1px solid #e3e3e3;border-bottom:0;background:#fafafa;padding:7px 9px}
.crumb{font-size:9.5px;color:var(--muted);margin-bottom:8px}
.photo-frame{width:198px;height:144px;border:1px dashed #cfcfcf;padding:3px;background:#fff}
.photo{width:100%;height:100%;background:radial-gradient(ellipse 45% 40% at 55% 55%,#2a2a2a 0,#2a2a2a 60%,#f2f2f2 100%)}
.card h4{font-size:14px;font-weight:400;color:var(--blue);line-height:18px;margin:8px 0 7px}
.card p{font-size:12px;line-height:18px;color:#222}
</style>
</head>
<body>
<div class="viewport">
<div class="page">

  <header>
    <div class="abs brand"><span class="brand-dot"></span><span class="brand-name">Lens Deal Ranger</span></div>

    <div class="abs compare">
      <svg width="34" height="36" viewBox="0 0 34 36" aria-hidden="true"><path d="M2 8 L14 0 L30 24 L22 30 Z" fill="var(--navy)"/><rect x="20" y="28" width="12" height="6" fill="var(--navy)"/></svg>
      <div><div class="compare-title">Comparison ▾</div><div class="compare-count">0 items</div></div>
    </div>
    <div class="abs nav-link" style="left:855px"><svg width="16" height="18" viewBox="0 0 16 18" aria-hidden="true"><path d="M3 15 L12 2 L15 4 L6 17 Z" fill="none" stroke="var(--navy)" stroke-width="2"/></svg>Articles</div>
    <div class="abs nav-link" style="left:908px"><svg width="26" height="18" viewBox="0 0 26 18" aria-hidden="true"><circle cx="9" cy="8" r="8" fill="var(--blue)"/><circle cx="18" cy="7" r="7" fill="var(--navy)"/></svg>Help</div>
    <div class="abs nav-link" style="left:965px"><svg width="22" height="18" viewBox="0 0 22 18" aria-hidden="true"><rect x="1" y="5" width="20" height="13" fill="var(--navy)"/><path d="M1 5 L11 13 L21 5" fill="none" stroke="#fff" stroke-width="1.5"/></svg>Contact</div>
  </header>

  <section class="abs filters">
    <div class="abs tabs">
      <div class="tab active" style="top:0"><div class="tab-thumb" role="img" aria-label="Compact camera" style="top:13px"></div></div>
      <div class="tab" style="top:51px"><div class="tab-thumb" role="img" aria-label="Camcorder" style="top:11px"></div></div>
      <div class="tab" style="top:96px"><div class="tab-thumb" role="img" aria-label="Lens" style="top:10px;left:18px;width:22px"></div></div>
    </div>

    <div class="group" style="left:58px;top:0;width:179px">
      <h3>Brand</h3>
      <ul><li class="on">Solvane <span>(488)</span></li><li class="on">Kasuro <span>(189)</span></li><li>Orbeline <span>(126)</span></li><li>Panterra <span>(235)</span></li></ul>
      <div class="more">more <i></i></div>
    </div>
    <div class="group" style="left:237px;top:0">
      <h3>Type</h3>
      <ul><li>Compact <span>(488)</span></li><li>SLR <span>(189)</span></li><li>Ultra zoom <span>(126)</span></li><li>Hybrid cameras <span>(235)</span></li></ul>
      <div class="more">more <i></i></div>
    </div>
    <div class="group" style="left:417px;top:0;width:181px">
      <h3>Zoom</h3>
      <ul><li>3x to 3,9x <span>(104)</span></li><li>5x to 7,9x <span>(189)</span></li><li>10x to 19,9x <span>(102)</span></li><li>more than 20x <span>(63)</span></li></ul>
      <div class="more">more <i></i></div>
    </div>
    <div class="group" style="left:598px;top:0">
      <h3>Picture Resolution</h3>
      <ul><li>8 to 10 Mpx <span>(846)</span></li><li class="on">11 to 15 Mpx <span>(235)</span></li><li class="on">16 to 17 Mpx <span>(195)</span></li><li class="on">more than 18 Mpx <span>(35)</span></li></ul>
      <div class="more">more <i></i></div>
    </div>
    <div class="group" style="left:778px;top:0;width:178px;border-right:0">
      <h3>Price</h3>
      <div class="price-input" style="left:12px">$ 80</div>
      <div class="to">to</div>
      <div class="price-input" style="left:103px">$ 9320</div>
      <div class="scale-label" style="left:35px">0.1k</div>
      <div class="scale-label" style="left:79px">1k</div>
      <div class="scale-label" style="left:115px">10k</div>
      <div class="track"><div class="track-fill"></div><div class="knob" style="left:18px"></div><div class="knob" style="left:98px"></div></div>
    </div>

    <div class="group" style="left:58px;top:150px;width:179px">
      <h3>Stabilization</h3>
      <ul><li class="on">Optical <span>(163)</span></li><li class="on">Digital <span>(278)</span></li><li class="on">Optical + Digital <span>(66)</span></li></ul>
    </div>
    <div class="group" style="left:237px;top:150px">
      <h3>Video Resolution</h3>
      <ul><li>1280 x 720 <span>(339)</span></li><li class="on">1920 x 1080 <span>(296)</span></li><li>320 x 240 <span>(8)</span></li><li>640 x 480 <span>(114)</span></li></ul>
      <div class="more">more <i></i></div>
    </div>
    <div class="group" style="left:417px;top:150px;width:181px">
      <h3>LCD Screen Size</h3>
      <ul><li>below 2,5 <span>(79)</span></li><li class="on">2,6 to 2,7 <span>(122)</span></li><li class="on">2,8 to 3,0 <span>(45)</span></li><li>more than 3,1 <span>(18)</span></li></ul>
      <div class="more">more <i></i></div>
    </div>
    <div class="group" style="left:598px;top:150px">
      <h3>Additional</h3>
      <ul><li>Watertight <span>(39)</span></li><li>GPS receiver <span>(87)</span></li><li>Moveable LCD <span>(32)</span></li></ul>
    </div>
    <div class="group" style="left:778px;top:150px;width:178px;border-right:0"></div>
  </section>

  <div class="abs search">
    <svg width="20" height="16" viewBox="0 0 20 16" aria-hidden="true"><circle cx="6" cy="5" r="4" fill="var(--navy)"/><path d="M0 16 Q6 8 12 16 Z" fill="var(--navy)"/><circle cx="13" cy="9" r="3.5" fill="none" stroke="var(--navy)" stroke-width="1.6"/><path d="M15.5 11.5 L19 15" stroke="var(--navy)" stroke-width="2"/></svg>
    Search
  </div>

  <ul class="abs sidebar">
    <li class="maker">Fenwa <span>(434)</span></li>
    <li class="maker">Kasuro <span>(342)</span></li>
    <li class="maker">Vortell <span>(319)</span></li>
    <li class="current">Solvane (316)</li>
    <li class="sub current">Photography</li>
    <li class="leaf">Category 1</li>
    <li class="leaf current">Category 2</li>
    <li class="leaf">Category 3</li>
    <li class="leaf">Category 4</li>
    <li class="sub">Camcorders</li>
  </ul>

  <svg class="abs section-icon" width="40" height="40" viewBox="0 0 40 40" aria-hidden="true">
    <rect x="2" y="10" width="28" height="28" rx="2" fill="var(--navy)"/>
    <circle cx="30" cy="9" r="8" fill="var(--blue)"/>
    <path d="M30 4 V14 M25 9 H35" stroke="#fff" stroke-width="2"/>
  </svg>
  <h2 class="abs section-title">Latest products</h2>

  <article class="abs card" style="left:317px">
    <div class="crumb">Solvane &gt; Photography &gt; Lorem</div>
    <div class="photo-frame"><div class="photo" role="img" aria-label="Black digital SLR camera with lens"></div></div>
    <h4>Curabitur pellentesque auctor pretium.</h4>
    <p>Lacus, et ultricies metus tempor cursus dictum arcu, vel porta ligula pulvinar in.</p>
  </article>
  <article class="abs card" style="left:557px">
    <div class="crumb">Vortell &gt; Camcorders &gt; Lorem</div>
    <div class="photo-frame"><div class="photo" role="img" aria-label="Black digital SLR camera with lens"></div></div>
    <h4>Lorem ipsum dolor sit amet, consectetur adipiscing.</h4>
    <p>Lacus, et ultricies metus tempor quis. Mauris lacinia tristique tellus a mattis. Aenean et velit at erat</p>
  </article>
  <article class="abs card" style="left:797px">
    <div class="crumb">Sarimo &nbsp;&gt; Photography &gt; Ipsum</div>
    <div class="photo-frame"><div class="photo" role="img" aria-label="Black digital SLR camera with lens"></div></div>
    <h4>Proin elementum rutrum tortor, quis mattis.</h4>
    <p>Velit at erat faucibus luctus in quis ligula cursus dictum arcu, vel porta ligula pulvinar in. Etiam eu auctor</p>
  </article>

</div>
</div>
</body>
</html>
```